Construction Site Sign

4' high x 8' wide construction site sign using the attached logo (small correction required) Utilize the red, white and blue colors; add the company address, telephone numbers and website.

418 Pellham Creek Lane, Suite 3
Millbrook, Georgia 30699
(706) 555-0182 Office
(706) 555-0139 Fax
www.ridgelinebuilders.biz

Industry/Entity Type

Construction

```html
<!DOCTYPE html>
<html lang="en">
<head>
<meta charset="utf-8">
<title>Ridgeline Builders – Site Sign</title>
<link rel="stylesheet" href="https://fonts.googleapis.com/css2?family=Questrial&display=swap">
<style>
  :root {
    --sign-white: #ffffff;
    --flag-red: #ec2028;
    --flag-red-edge: #a8282e;
    --flag-blue: #0c56a4;
    --flag-blue-edge: #1e4b86;
    --steel-gray: #a7a9ac;
    --steel-gray-edge: #7b7d80;
    --ink: #1a1a1a;
  }
  * { margin: 0; padding: 0; box-sizing: border-box; }
  html, body {
    width: 1200px;
    height: 660px;
    overflow: hidden;
    background: var(--sign-white);
  }
  .site-sign {
    position: relative;
    width: 1200px;
    height: 660px;
    background: var(--sign-white);
    font-family: "Questrial", sans-serif;
  }
  .sign-bands {
    position: absolute;
    inset: 0;
  }
  .company-name {
    position: absolute;
    left: 0;
    right: 0;
    top: 250px;
    text-align: center;
    font-size: 62px;
    letter-spacing: 2px;
    text-transform: uppercase;
    color: var(--flag-blue);
    font-weight: 400;
  }
  .contact-block {
    position: absolute;
    left: 0;
    right: 0;
    top: 422px;
    text-align: center;
    font-size: 25px;
    line-height: 29px;
    letter-spacing: 1px;
    color: var(--ink);
    font-style: normal;
  }
</style>
</head>
<body>
<main class="site-sign">
  <svg class="sign-bands" width="1200" height="660" viewBox="0 0 1200 660" aria-hidden="true">
    <polygon points="0,99 323,354 236,660 0,660" fill="var(--flag-red-edge)"/>
    <polygon points="0,109 323,362 236,660 0,660" fill="var(--flag-red)"/>
    <polygon points="1200,99 876,354 964,660 1200,660" fill="var(--flag-blue-edge)"/>
    <polygon points="1200,109 876,362 964,660 1200,660" fill="var(--flag-blue)"/>
    <polygon points="599,581 497,660 703,660" fill="var(--steel-gray-edge)"/>
    <polygon points="599,590 509,660 691,660" fill="var(--steel-gray)"/>
  </svg>

  <h1 class="company-name">Ridgeline Builders</h1>

  <address class="contact-block">
    418 Pellham Creek Lane, Suite 3<br>
    Millbrook, Georgia 30699<br>
    (706) 555-0182 Office, (706) 555-0139 Fax<br>
    www.ridgelinebuilders.biz
  </address>
</main>
</body>
</html>
```